Solo consultant in research/analytics/data science space needs new business card

I need a new business card to promote my solo business as creative problem solver and consultant. I work on business projects for sales and market research and analytics, customer/market insights, and data science. I provide clients data-informed insights and ideas to enhance their businesses. My initial tagline: 'Make your data work for YOU.'

People should hire me because of my diverse background. Because of my Ph.D. in Political Science I have a strong background in research and analytics, project design and management, and communications skills. With my experience as a marketing analyst, a volunteer on non-profit projects, and currently as research consultant I have worked on projects within various industries. I also have a taste for improvisation so I enjoy thinking creatively and appreciate design thinking.

As an introduction to my background: Clients might want to hire me for many types of projects. Clients might wish to understand who their best customers are and how to characterize them. Maybe clients want to know how their customers feel about a certain product or service. Clients might want to know more about their local market area and overall industry. Clients might want to know whether their marketing programs are effective or else what drives their sales revenue. Perhaps clients want to use their data to create something useful for themselves or their customers.

One client hired me to help them decide whether to expand their services to newer customers. I gathered and analyzed information about the local area – the characteristics of people living there as well as the client’s competitors – and described trends and implications. The client was very pleased with the results and submitted them to superiors for approval to move forward.

For another client – who was looking to purchase a house in a metropolitan area – I gathered population and school data about the area. With this, I created an interactive mapping tool so they could zoom in on neighborhoods and learn more about them before they selected a neighborhood to purchase a house. They were happy with the results of my work.

When I worked as a marketing analyst for a consulting firm, a Vice President of Marketing hired us to discover whether or not the company’s marketing programs (i.e. coupons and discounts) were effective. I analyzed their data and our team discovered their marketing was indeed effective. He was very happy and used this to justify their programs to the Finance department (who thought such programs lost revenue).

- Marcus Delano Whitby, Ph.D.

Target Market(s)

Future clients and employers. The most immediate target markets will be other service providers such as consulting companies, marketing firms and ad agencies. I will also use this for meeting with clients in various industries.

Industry/Entity Type

Consulting

Contact Information for Business Card

Since it is my first real business card as a solo practitioner, I want to make an excellent first impression. I want this useful in case someone hires me to work on projects or else hire me to work within a firm or company. The card should convey competence and some creativity while also being neither stuffy nor a data geek.

Colors

Designer to choose colors to be used in the design.

Requirements
Nice to have
• Attached are the starting efforts at the card to add some color. It will be nice to use my name and descriptors on one side and tagline on the other. If anyone has better ideas, I will love to see them!

```html
<!DOCTYPE html>
<html lang="en">
<head>
<meta charset="utf-8">
<title>Marcus Delano Whitby, Ph.D. — Business Card</title>
<link href="https://fonts.googleapis.com/css2?family=Arimo:wght@400&family=Noto+Sans:wght@400;800&display=swap" rel="stylesheet">
<style>
  :root {
    --page: #ffffff;
    --charcoal: #2d2d2d;
    --coral: #e05d4b;
    --cream: #f8eedd;
    --ink: #111111;
    --card-shadow: 10px 12px 14px rgba(0,0,0,0.45);
  }
  html, body {
    margin: 0;
    padding: 0;
    width: 1200px;
    height: 1200px;
    overflow: hidden;
    background: var(--page);
  }
  .canvas {
    position: relative;
    width: 1200px;
    height: 1200px;
  }
  .card {
    position: absolute;
    left: 238px;
    width: 692px;
    height: 401px;
    border-radius: 20px;
    box-shadow: var(--card-shadow);
    overflow: hidden;
  }
  /* Tagline side */
  .card--tagline {
    top: 150px;
    background: var(--charcoal);
  }
  .tagline {
    position: absolute;
    left: 0;
    right: 0;
    top: 118px;
    margin: 0;
    text-align: center;
    font-family: "Arimo", Arial, sans-serif;
    font-weight: 400;
    font-size: 61px;
    line-height: 83px;
    color: #ffffff;
    padding-left: 18px;
  }
  /* Contact side */
  .card--contact {
    top: 619px;
    background: #ffffff;
  }
  .header-band {
    position: absolute;
    left: 0; top: 0; right: 0;
    height: 185px;
    background: var(--coral);
  }
  .name {
    position: absolute;
    left: 49px;
    top: 69px;
    margin: 0;
    font-family: "Noto Sans", Verdana, sans-serif;
    font-weight: 800;
    font-size: 38.5px;
    letter-spacing: 0;
    line-height: 1;
    color: var(--cream);
    white-space: nowrap;
  }
  .disciplines {
    position: absolute;
    left: 50px;
    top: 120px;
    margin: 0;
    font-family: "Noto Sans", Verdana, sans-serif;
    font-size: 21.5px;
    line-height: 1;
    color: var(--ink);
    white-space: nowrap;
  }
  .role {
    position: absolute;
    left: 50px;
    top: 233px;
    font-family: "Noto Sans", Verdana, sans-serif;
    font-size: 27px;
    line-height: 1;
    color: var(--coral);
  }
  .location {
    position: absolute;
    left: 50px;
    top: 262px;
    font-family: "Noto Sans", Verdana, sans-serif;
    font-size: 19px;
    line-height: 1;
    color: var(--ink);
  }
  .phone {
    position: absolute;
    left: 50px;
    top: 293px;
    font-family: "Arimo", Arial, sans-serif;
    font-size: 22px;
    line-height: 1;
    color: var(--ink);
  }
  .divider {
    position: absolute;
    left: 342px;
    top: 203px;
  }
  .contact-list {
    position: absolute;
    left: 386px;
    top: 233px;
    margin: 0;
    padding: 0;
    list-style: none;
    font-family: "Arimo", Arial, sans-serif;
    font-size: 19px;
    color: var(--ink);
  }
  .contact-list li {
    position: relative;
    padding-left: 44px;
    height: 22px;
    line-height: 22px;
    white-space: nowrap;
  }
  .contact-list li + li { margin-top: 14px; }
  .contact-list li:last-child { margin-top: 8px; }
  .contact-icon {
    position: absolute;
    left: 0;
    top: 1px;
  }
</style>
</head>
<body>
<main class="canvas">

  <section class="card card--tagline">
    <p class="tagline">Make your data<br>work for YOU.</p>
  </section>

  <section class="card card--contact">
    <div class="header-band"></div>
    <h1 class="name">Marcus Delano Whitby, Ph.D.</h1>
    <p class="disciplines">Research/Analytics – Customer Intelligence – Data Science</p>

    <div class="role">Consultant</div>
    <div class="location">Lisbon, PT</div>
    <div class="phone">+351 912 640 318</div>

    <svg class="divider" width="4" height="160" viewBox="0 0 4 160" aria-hidden="true">
      <path d="M2 0 C3.6 50 3.6 110 2 160 C0.4 110 0.4 50 2 0 Z" fill="var(--charcoal)"/>
    </svg>

    <ul class="contact-list">
      <li>
        <svg class="contact-icon" width="24" height="20" viewBox="0 0 24 20" aria-hidden="true">
          <rect x="2" y="4" width="20" height="13" fill="none" stroke="#111" stroke-width="2"/>
          <path d="M2 4 L12 12 L22 4 M2 17 L9 10 M22 17 L15 10" fill="none" stroke="#111" stroke-width="1.8"/>
        </svg>
        mdwhitby70@inboxmail.net
      </li>
      <li>
        <svg class="contact-icon" width="24" height="22" viewBox="0 0 24 22" aria-hidden="true">
          <circle cx="12" cy="11" r="10" fill="#1da1e0"/>
        </svg>
        @MarcusWhitby70
      </li>
      <li>
        <svg class="contact-icon" width="24" height="22" viewBox="0 0 24 22" aria-hidden="true">
          <circle cx="12" cy="11" r="9" fill="none" stroke="#111" stroke-width="2"/>
          <ellipse cx="12" cy="11" rx="4" ry="9" fill="none" stroke="#111" stroke-width="1.5"/>
          <path d="M3 11 H21 M5 6 H19 M5 16 H19" stroke="#111" stroke-width="1.3"/>
        </svg>
        Marcuswhitby.net
      </li>
    </ul>
  </section>

</main>
</body>
</html>
```